Women's Online Clothing Boutique Needs Business Cards

I already have a logo that I would like to use. Some of the things that interest me is black business cards, foil embossed logo, glossy embossed logo, leopard print, no yellow font, rounded edges. I even like just a large logo on the front side with all of my information on the back side.

Contact Information for Business Card

https://silverheron.shopvenlo.com/
https://www.pagelink.net/thesilverheronboutique/
https://www.picfeed.net/thesilverheronboutique/
silverheronboutique@mailora.net

Requirements
Must have
• My Logo
Nice to have
• Leopard Print
Should not have
• No Yellow Font

```html
<!DOCTYPE html>
<html lang="en">
<head>
<meta charset="utf-8">
<title>The Silver Heron Boutique – Business Cards</title>
<link rel="stylesheet" href="https://fonts.googleapis.com/css2?family=Montserrat:wght@400;500;700&display=swap">
<style>
  :root {
    --page-bg: #ffffff;
    --card-bg: #000000;
    --wave-1: #0d0d0d;
    --wave-2: #151515;
    --wave-3: #1c1c1c;
    --gold: #c8922a;
    --text-light: #ffffff;
    --text-muted: #e6e6e6;
  }
  * { box-sizing: border-box; margin: 0; padding: 0; }
  html, body {
    width: 960px; height: 1200px; overflow: hidden;
    background: var(--page-bg);
    font-family: "Montserrat", sans-serif;
  }
  .canvas {
    position: relative; width: 960px; height: 1200px;
    display: flex; flex-direction: column; align-items: center; justify-content: center; gap: 80px;
  }
  .card {
    position: relative; width: 760px; height: 434px;
    background: var(--card-bg); border-radius: 22px; overflow: hidden;
    box-shadow: 0 10px 30px rgba(0,0,0,0.22);
  }
  .card-waves { position: absolute; left: 0; bottom: 0; width: 100%; height: 150px; }
  .brand {
    position: absolute; display: flex; flex-direction: column; align-items: center;
    color: var(--gold); font-weight: 500; text-align: center; line-height: 1.1;
  }
  .brand-dot { width: 34px; height: 34px; border-radius: 50%; background: var(--gold); margin-bottom: 14px; }
  .card-front .brand { left: 0; right: 0; top: 118px; font-size: 44px; }
  .card-front .brand-name small { display: block; font-size: 44px; }
  .card-back .brand { left: 40px; width: 320px; top: 142px; font-size: 28px; }
  .card-back .brand-dot { width: 24px; height: 24px; margin-bottom: 10px; }
  .divider { position: absolute; left: 361px; top: 108px; width: 2px; height: 183px; background: var(--gold); }
  .contact { position: absolute; left: 406px; top: 118px; color: var(--text-light); }
  .contact-name { font-weight: 700; font-size: 23px; letter-spacing: 0.5px; text-transform: uppercase; }
  .contact-role { font-size: 13px; margin-top: 6px; color: var(--text-muted); }
  .contact-list { list-style: none; margin-top: 36px; }
  .contact-list li { display: flex; align-items: center; gap: 12px; font-size: 13.5px; height: 31px; }
  .contact-list li:first-child { font-size: 15px; }
  .contact-list svg { width: 15px; height: 15px; flex: none; }
</style>
</head>
<body>
<main class="canvas">

  <section class="card card-front" aria-label="Business card front">
    <div class="brand">
      <span class="brand-dot"></span>
      <span class="brand-name">The Silver Heron<small>Boutique</small></span>
    </div>
    <svg class="card-waves" viewBox="0 0 760 150" preserveAspectRatio="none" aria-hidden="true">
      <path d="M0 150 C120 40 260 40 420 80 C560 115 680 90 760 10 L760 150 Z" fill="var(--wave-3)"/>
      <path d="M0 150 C140 70 280 60 430 100 C570 135 680 120 760 60 L760 150 Z" fill="var(--wave-2)"/>
      <path d="M0 150 C160 100 300 95 450 125 C580 148 690 140 760 110 L760 150 Z" fill="var(--wave-1)"/>
    </svg>
  </section>

  <section class="card card-back" aria-label="Business card back">
    <div class="brand">
      <span class="brand-dot"></span>
      <span class="brand-name">The Silver Heron<br>Boutique</span>
    </div>
    <div class="divider"></div>
    <div class="contact">
      <h1 class="contact-name">Marlene Okafor</h1>
      <p class="contact-role">Fashion Designer</p>
      <ul class="contact-list">
        <li>
          <svg viewBox="0 0 24 24" aria-hidden="true"><path fill="var(--gold)" d="M6.6 10.8a15.1 15.1 0 0 0 6.6 6.6l2.2-2.2c.3-.3.7-.4 1-.2 1.1.4 2.3.6 3.6.6.6 0 1 .4 1 1V20c0 .6-.4 1-1 1C10.6 21 3 13.4 3 4c0-.6.4-1 1-1h3.5c.6 0 1 .4 1 1 0 1.3.2 2.5.6 3.6.1.3 0 .7-.2 1z"/></svg>
          1 555-210-4837
        </li>
        <li>
          <svg viewBox="0 0 24 24" aria-hidden="true"><rect x="2" y="5" width="20" height="14" rx="1.5" fill="var(--gold)"/><path d="M3 6l9 7 9-7" stroke="var(--card-bg)" stroke-width="1.6" fill="none"/></svg>
          silverheronboutique@mailora.net
        </li>
        <li>
          <svg viewBox="0 0 24 24" aria-hidden="true"><g fill="none" stroke="var(--gold)" stroke-width="1.8"><circle cx="12" cy="12" r="9.5"/><ellipse cx="12" cy="12" rx="4.2" ry="9.5"/><path d="M2.5 12h19M4 7h16M4 17h16"/></g></svg>
          silverheron.shopvenlo.com
        </li>
      </ul>
    </div>
    <svg class="card-waves" viewBox="0 0 760 150" preserveAspectRatio="none" aria-hidden="true">
      <path d="M0 150 C120 40 260 40 420 80 C560 115 680 90 760 10 L760 150 Z" fill="var(--wave-3)"/>
      <path d="M0 150 C140 70 280 60 430 100 C570 135 680 120 760 60 L760 150 Z" fill="var(--wave-2)"/>
      <path d="M0 150 C160 100 300 95 450 125 C580 148 690 140 760 110 L760 150 Z" fill="var(--wave-1)"/>
    </svg>
  </section>

</main>
</body>
</html>
```